Guide to Internet of Things Connectivity in Social Housing

THE SIZE of the booklet is A4.
We are producing a guide to the different types of internet of things (IoT) connectivity technology in the context of UK social housing.
The guide simply explains these technologies and provides examples of where they might be relevant in social housing.
The guide need a cover and feature a different technology on each page(wifi, z-wave, Bluetooth etc). It would be great to use some graphics to bring the pages to life and communicate a sense of 'networked connectivity' if it is possible to use logos for some of these technologies without copyright issues this could be good.
Ideally the guide will fit with our current organisation branding of black and gold/yellow.
Our website is www.tallowquay.io
FOR THE INITIAL ENTRIES:
I am happy for you to do a sample of the cover/back and some internal pages but no need to do all the pages at this stage.
Social Housing sector Professionals
Internet

```html
<!DOCTYPE html>
<html lang="en">
<head>
<meta charset="utf-8">
<title>IoT Connectivity for UK Housing – Cover</title>
<link href="https://fonts.googleapis.com/css2?family=Montserrat:wght@500;700;800&display=swap" rel="stylesheet">
<style>
  :root {
    --charcoal: #2a2a2a;
    --night: #0b0804;
    --gold: #f5c300;
    --amber: #f2a205;
    --glow: #ffd27a;
    --ember: #c77a12;
    --white: #ffffff;
  }
  * { margin: 0; padding: 0; box-sizing: border-box; }
  html, body { width: 851px; height: 1200px; overflow: hidden; background: var(--white); }
  .cover {
    position: relative;
    width: 851px;
    height: 1200px;
    font-family: "Montserrat", Arial, sans-serif;
    overflow: hidden;
  }
  .masthead {
    position: absolute;
    inset: 0 0 auto 0;
    height: 283px;
    background: var(--charcoal);
  }
  .brand {
    position: absolute;
    left: 56px;
    top: 52px;
    display: flex;
    flex-direction: column;
    gap: 20px;
  }
  .brand-square {
    width: 62px;
    height: 62px;
    background: var(--gold);
  }
  .brand-name {
    color: var(--gold);
    font-weight: 500;
    font-size: 36px;
    line-height: 1.05;
    letter-spacing: 0.3px;
    text-transform: uppercase;
  }
  .hero-visual {
    position: absolute;
    top: 283px;
    left: 0;
    width: 851px;
    height: 637px;
    background:
      radial-gradient(ellipse 170px 150px at 60px 300px, rgba(255,226,150,0.95), rgba(245,180,60,0.55) 55%, transparent 100%),
      radial-gradient(ellipse 360px 400px at 90px 330px, rgba(240,165,40,0.85), rgba(199,122,18,0.45) 50%, transparent 80%),
      radial-gradient(ellipse 260px 90px at 430px 60px, rgba(255,200,90,0.45), transparent 75%),
      radial-gradient(ellipse 220px 130px at 520px 230px, rgba(230,150,30,0.5), transparent 75%),
      radial-gradient(ellipse 180px 110px at 720px 90px, rgba(255,190,80,0.35), transparent 75%),
      radial-gradient(ellipse 240px 120px at 330px 480px, rgba(220,140,30,0.45), transparent 75%),
      radial-gradient(ellipse 200px 100px at 780px 330px, rgba(240,170,60,0.3), transparent 75%),
      radial-gradient(ellipse 260px 120px at 600px 560px, rgba(180,105,20,0.4), transparent 75%),
      linear-gradient(160deg, rgba(120,70,10,0.25), transparent 55%),
      var(--night);
  }
  .title-band {
    position: absolute;
    top: 920px;
    left: 0;
    width: 851px;
    height: 280px;
    background: var(--amber);
    padding: 50px 56px 0;
    color: var(--white);
  }
  .title {
    font-weight: 800;
    font-size: 47px;
    line-height: 1;
    letter-spacing: 0.4px;
  }
  .subtitle {
    margin-top: 12px;
    font-weight: 700;
    font-size: 24px;
    letter-spacing: 0.5px;
  }
</style>
</head>
<body>
  <main class="cover">
    <header class="masthead">
      <div class="brand">
        <span class="brand-square" aria-hidden="true"></span>
        <p class="brand-name">Tallow Quay<br>Consortium</p>
      </div>
    </header>
    <div class="hero-visual" role="img" aria-label="Glowing gold network of connected points and lines spreading across a dark globe, with floating data figures, suggesting networked connectivity"></div>
    <section class="title-band">
      <h1 class="title">IoT CONNECTIVITY</h1>
      <p class="subtitle">FOR UK HOUSING</p>
    </section>
  </main>
</body>
</html>
```